Banner Design for Brisk Loans

Hi,

I know this is under flyer design, however, I am actually after a Banner (I could not find this option). The banner needs to be done to fit the following specifications.

1 x 850mm W x 1500mm H Double Sided Luxury Retractable

I have provided a banner which I currently have however, I would like it to be updated.

I would like to banners created.

Banner 1

The banner should still maintain the lender logos and the fact we assess over 30 lenders, plus also promote the 'Brisk Loans' logo.

Along with this is I would like to promote the 'Brisk Cost Refund.'

Also have the wording
'We Cover your Discharge fee and new loan application fee'
also may use this link as guidance http://www.briskloansdemo.com.au/briskrefund/

Banner 2

This banner I would like it to promote a 'Quick Mortgage Health Check'.

Also include 'The Brisk Loans Edge'

http://www.briskloansdemo.com.au/briskrefund/

Again use this as a guide as to the 4 points of difference, you may use different icons if you feel it looks better

Target Market(s)

People with Home Loans

Industry/Entity Type

Finance

Font styles to use
Sans Serif

Colors
ec1f27
ffffff

Requirements
Must have
• As per the description
Nice to have
• Professional look, good icons to accompany wording
Should not have
• unprofessional look too much text or cluttered

```html
<!DOCTYPE html>
<html lang="en">
<head>
<meta charset="utf-8">
<title>Brisk Loans – Brisk Cost Refund Banner</title>
<link rel="stylesheet" href="https://fonts.googleapis.com/css2?family=Cinzel:wght@600;700&family=Oswald:wght@500;600;700&display=swap">
<style>
  :root {
    --brand-red: #ec1f27;
    --deep-red: #c8161d;
    --ink: #2b2b2b;
    --charcoal: #333333;
    --muted: #5a5a5a;
    --paper: #ffffff;
    --rule: #bdbdbd;
  }
  * { margin: 0; padding: 0; box-sizing: border-box; }
  html, body { width: 768px; height: 1200px; overflow: hidden; background: var(--paper); }
  .banner {
    position: relative;
    width: 768px;
    height: 1200px;
    background: var(--paper);
    overflow: hidden;
  }
  .brand {
    position: absolute;
    top: 70px; left: 0; right: 0;
    text-align: center;
  }
  .brand-name {
    display: inline-flex;
    align-items: center;
    gap: 18px;
    font-family: "Cinzel", serif;
    font-weight: 700;
    font-size: 66px;
    color: var(--ink);
    letter-spacing: 1px;
  }
  .brand-mark {
    width: 52px; height: 52px;
    background: var(--brand-red);
  }
  .brand-tagline {
    margin-top: 10px;
    font-family: "Cinzel", serif;
    font-weight: 700;
    font-size: 22px;
    color: var(--ink);
  }
  .brand-rule {
    position: absolute;
    top: 240px; left: 140px; right: 140px;
    height: 2px;
    background: var(--rule);
  }
  .offer-title {
    position: absolute;
    top: 270px; left: 0; right: 0;
    text-align: center;
    font-family: "Oswald", sans-serif;
    font-weight: 700;
    color: var(--brand-red);
    text-transform: uppercase;
    line-height: 1;
  }
  .offer-title .line-one { display: block; font-size: 112px; letter-spacing: 4px; }
  .offer-title .line-two { display: block; font-size: 128px; letter-spacing: 2px; margin-top: 8px; }
  .cover-box {
    position: absolute;
    top: 600px; left: 50px; right: 50px;
    height: 200px;
    background: linear-gradient(180deg, #4a4a4a 0%, var(--charcoal) 100%);
    border: 3px solid var(--brand-red);
    padding-top: 62px;
    text-align: center;
    font-family: "Oswald", sans-serif;
    font-weight: 700;
    color: var(--paper);
    text-transform: uppercase;
    font-size: 48px;
    line-height: 1.1;
  }
  .cover-tab {
    position: absolute;
    top: 568px; left: 50%;
    transform: translateX(-50%);
    width: 390px; height: 72px;
    background: var(--brand-red);
    border-radius: 8px;
    text-align: center;
    font-family: "Oswald", sans-serif;
    font-weight: 700;
    font-size: 50px;
    line-height: 72px;
    color: var(--paper);
    letter-spacing: 2px;
  }
  .lenders-band {
    position: absolute;
    top: 830px; left: 0; right: 0;
    height: 62px;
    background: var(--brand-red);
    text-align: center;
    font-family: "Cinzel", serif;
    font-weight: 700;
    font-size: 32px;
    line-height: 62px;
    color: var(--paper);
    letter-spacing: 1px;
  }
  .lender-grid {
    position: absolute;
    top: 920px; left: 30px; right: 30px;
    display: grid;
    grid-template-columns: repeat(5, 1fr);
    row-gap: 34px;
    column-gap: 10px;
    text-align: center;
  }
  .lender {
    display: flex;
    align-items: center;
    justify-content: center;
    gap: 6px;
    font-family: "Oswald", sans-serif;
    font-weight: 500;
    font-size: 19px;
    color: var(--muted);
    white-space: nowrap;
  }
  .lender-dot {
    width: 12px; height: 12px;
    background: var(--brand-red);
    border-radius: 50%;
  }
  .footer-url {
    position: absolute;
    bottom: 0; left: 0; right: 0;
    height: 90px;
  }
  .footer-url svg { position: absolute; inset: 0; }
  .footer-url span {
    position: absolute;
    inset: 0;
    text-align: center;
    line-height: 100px;
    font-family: "Cinzel", serif;
    font-weight: 700;
    font-size: 30px;
    color: var(--paper);
    letter-spacing: 1px;
  }
</style>
</head>
<body>
  <main class="banner">
    <header class="brand">
      <div class="brand-name"><span class="brand-mark"></span>Brisk Loans</div>
      <p class="brand-tagline">IS YOUR HOME LOAN WORKING HARD?</p>
    </header>
    <div class="brand-rule"></div>

    <h1 class="offer-title">
      <span class="line-one">Brisk Cost</span>
      <span class="line-two">Refund</span>
    </h1>

    <section class="cover-box">Your discharge fee and<br>new loan application fee</section>
    <div class="cover-tab">WE COVER</div>

    <div class="lenders-band">We Assess Over 30 Lenders</div>

    <section class="lender-grid" aria-label="Lenders assessed">
      <div class="lender">Lumen Savings</div>
      <div class="lender">Kestrel Finance</div>
      <div class="lender"><span class="lender-dot"></span>Alder Bank</div>
      <div class="lender">Crestview</div>
      <div class="lender">Tidewater</div>
      <div class="lender">Granite Mutual</div>
      <div class="lender">Quarry Credit</div>
      <div class="lender">Homestead Co</div>
      <div class="lender">Juniper</div>
      <div class="lender">Basalt Capital</div>
      <div class="lender">Meridian Trust</div>
      <div class="lender">Larkspur Bank</div>
      <div class="lender">Ashgrove</div>
      <div class="lender"><span class="lender-dot"></span>Northvale</div>
      <div class="lender">Cobalt Mutual</div>
    </section>

    <footer class="footer-url">
      <svg width="768" height="90" viewBox="0 0 768 90" aria-hidden="true">
        <polygon points="60,0 708,0 768,90 0,90" fill="var(--brand-red)"/>
        <polygon points="0,90 60,0 40,0 0,60" fill="var(--deep-red)"/>
      </svg>
      <span>WWW.BRISKLOANSDEMO.COM.AU</span>
    </footer>
  </main>
</body>
</html>
```